Business card design needed

I am a small start up business in the mortgage broking industry based in Sydney called 'keys2nest'. I will be providing residential mortgages to first home owners, investors and people looking to refinance. I would like to see designs that use the colors blue, black, and white - same as my logo (see logo design uploaded)

Target Market(s)

My target market is First Home Owners, property investors, and people looking to refinance. The loans I will be providing are for residential property only at this stage, and my clients will predominantly be in the 30-50yr age bracket.

Industry/Entity Type

Residential

Contact Information for Business Card

Owen Partridge
Director/Mobile Mortgage Broker
keys2nest
PO BOX 4287
Westmead NSW 2145
Mb: 0491 862 307
email: owen@keys2nest.com.au

Requirements
Must have
• please use lower case for business name (i.e. keys2nest)

```html
<!DOCTYPE html>
<html lang="en">
<head>
<meta charset="utf-8">
<title>keys2nest business card</title>
<link rel="stylesheet" href="https://fonts.googleapis.com/css2?family=Questrial&display=swap">
<style>
  :root {
    --blue: #1ba1e2;
    --ink: #222222;
    --ink-soft: #3a3a3a;
    --paper: #ffffff;
    --charcoal: #2d2d2d;
    --stage: #dfe5e8;
  }
  * { margin: 0; padding: 0; box-sizing: border-box; }
  html, body {
    width: 1200px; height: 960px; overflow: hidden;
    background: var(--stage);
    font-family: "Questrial", "Century Gothic", sans-serif;
  }
  .card {
    position: absolute; left: 250px;
    width: 700px; height: 400px;
    box-shadow: 0 6px 18px rgba(0,0,0,.18);
    overflow: hidden;
  }
  .card--front { top: 50px; background: var(--paper); color: var(--ink); }
  .card--back  { top: 500px; background: var(--charcoal); color: var(--paper); }

  .brand {
    position: absolute; display: flex; align-items: center; gap: 12px;
    font-size: 52px; letter-spacing: -1px; line-height: 1;
  }
  .brand__mark { width: 34px; height: 34px; background: var(--blue); }
  .card--front .brand { left: 42px; top: 78px; color: var(--ink); }
  .card--back .brand { left: 50%; top: 50%; transform: translate(-50%, -50%); color: var(--paper); font-size: 60px; }

  .holder { position: absolute; left: 42px; top: 262px; }
  .holder__name { font-size: 29px; letter-spacing: 1px; text-transform: uppercase; color: var(--ink); }
  .holder__role { font-size: 17px; color: var(--ink-soft); margin-top: 6px; }

  .contact {
    position: absolute; left: 375px; top: 232px;
    list-style: none; font-size: 15px; color: var(--ink-soft);
  }
  .contact li { display: flex; align-items: center; gap: 12px; height: 24px; }
  .contact svg { width: 14px; height: 14px; flex: none; fill: none; stroke: var(--blue); stroke-width: 1.6; }
  .contact .icon-home { fill: var(--blue); stroke: none; }

  .accent-bar { position: absolute; bottom: 0; height: 9px; background: var(--blue); }
  .card--front .accent-bar { left: 48px; width: 270px; }
  .card--back .accent-bar { left: 370px; width: 230px; }
</style>
</head>
<body>

<section class="card card--front">
  <div class="brand"><span class="brand__mark"></span><span class="brand__name">keys2nest</span></div>

  <div class="holder">
    <p class="holder__name">Owen Partridge</p>
    <p class="holder__role">Director/Mobile Mortgage Broker</p>
  </div>

  <ul class="contact">
    <li>
      <svg viewBox="0 0 14 14" aria-hidden="true"><rect x="3.5" y="1" width="7" height="12" rx="1.2"/><line x1="6" y1="11" x2="8" y2="11"/></svg>
      <span>0491 862 307</span>
    </li>
    <li>
      <svg viewBox="0 0 14 14" aria-hidden="true"><rect x="1" y="3" width="12" height="8.5"/><polyline points="1,3 7,8 13,3"/></svg>
      <span>owen@keys2nest.com.au</span>
    </li>
    <li>
      <svg class="icon-home" viewBox="0 0 14 14" aria-hidden="true"><polygon points="7,1 13.5,7 11.5,7 11.5,13 8.5,13 8.5,9 5.5,9 5.5,13 2.5,13 2.5,7 0.5,7"/></svg>
      <span>PO BOX 4287 Westmead NSW 2145</span>
    </li>
  </ul>

  <div class="accent-bar"></div>
</section>

<section class="card card--back">
  <div class="brand"><span class="brand__mark"></span><span class="brand__name">keys2nest</span></div>
  <div class="accent-bar"></div>
</section>

</body>
</html>
```